Stand bag for exclusive, natural snacks

We are looking for a PP stand bag design that will be used to pack exclusive snacks (dried fruits). These snacks will be 100% natural, healthy and without any chemicals. For that reason and for the fact that these products will have a higher price point, the stand bag design should look very premium and happy, while still reminding the customer of the natural, healthy benefits of the snacks inside. The main colors of our brand are black and gold, so we would like to see the packaging in similar colors. In order to be able to see the product, we usually leave some part of the PP packaging transparent.
Packaging Size: h170mm x w80mm x d30mm

Target Market(s)

High-end retail markets with consumers that are willing to pay a little more to get a high-quality product, free from any preservatives and completely natural.

Font styles to use
Sans Serif

Colors

Designer to choose colors to be used in the design.

Requirements
Must have
• - similar to the bag in the sample photos
• - bag size: h170mm x w80mm x d30mm
• - Our logo
• - the colors black & gold
• - Some way of showing the customer the benefit of our dried fruits (healthy, natural, happy)
• - a transparent part to see the product through the plastic foil
Nice to have
• - bottom maybe not transparent in order not to see dust that falls to the bottom

```html
<!DOCTYPE html>
<html lang="en">
<head>
<meta charset="utf-8">
<title>Aurel Pantry – Pomelo and Coconut Meet Almonds – Stand Bag Front</title>
<link href="https://fonts.googleapis.com/css2?family=Montserrat:wght@600;700;800&family=Oswald:wght@300&display=swap" rel="stylesheet">
<style>
  :root {
    --canvas: #ffffff;
    --pattern-light: #e4e5e7;
    --ink-black: #0b0b0b;
    --gold-deep: #7d6434;
    --gold-mid: #b8975a;
    --gold-light: #d7bf86;
    --ribbon-gold: #c9ad72;
    --label-white: #f4f4f4;
    --weight-grey: #9a9a9a;
    --window-tan: #c99a6e;
    --window-cream: #ece4d8;
  }
  * { margin: 0; padding: 0; box-sizing: border-box; }
  html, body {
    width: 1200px;
    height: 1000px;
    overflow: hidden;
    background: var(--canvas);
  }
  .bag-front {
    position: absolute;
    left: 362px;
    top: 50px;
    width: 476px;
    height: 900px;
    overflow: hidden;
  }
  .leaf-pattern-area {
    position: absolute;
    left: 0; top: 0;
    width: 100%; height: 523px;
    background: linear-gradient(180deg, #e9eaec 0%, var(--pattern-light) 100%);
  }
  .fruit-illustration-area {
    position: absolute;
    left: 0; top: 527px;
    width: 100%; height: 373px;
    background: radial-gradient(ellipse at 50% 70%, #1a1a1a 0%, var(--ink-black) 70%);
  }
  .gold-divider {
    position: absolute;
    left: 0; top: 521px;
    width: 100%; height: 7px;
    background: linear-gradient(90deg, var(--gold-deep), var(--gold-light) 50%, var(--gold-deep));
  }
  .brand-ribbon {
    position: absolute;
    left: 192px; top: 0;
    width: 92px; height: 192px;
  }
  .brand-name {
    position: absolute;
    left: 0; top: 100px;
    width: 100%;
    text-align: center;
    font-family: "Montserrat", sans-serif;
    font-weight: 700;
    font-size: 22px;
    letter-spacing: 3px;
    color: var(--ink-black);
    line-height: 1;
  }
  .product-title {
    position: absolute;
    left: 0; top: 222px;
    width: 100%;
    text-align: center;
    font-family: "Montserrat", sans-serif;
    font-weight: 800;
    font-size: 45px;
    line-height: 46px;
    letter-spacing: -0.5px;
    background: linear-gradient(100deg, var(--gold-deep) 10%, var(--gold-mid) 45%, var(--gold-light) 60%, var(--gold-deep) 90%);
    -webkit-background-clip: text;
    background-clip: text;
    color: transparent;
  }
  .product-window {
    position: absolute;
    left: 149px; top: 434px;
    width: 178px; height: 177px;
    border: 5px solid var(--gold-mid);
    background: linear-gradient(135deg, var(--window-tan) 0%, var(--window-cream) 35%, var(--window-tan) 60%, var(--window-cream) 85%);
    box-shadow: inset 0 0 0 1px var(--gold-light);
  }
  .quality-claim {
    position: absolute;
    left: 0; top: 624px;
    width: 100%;
    text-align: center;
    font-family: "Montserrat", sans-serif;
    font-weight: 700;
    font-size: 16px;
    letter-spacing: 0.3px;
    color: var(--label-white);
  }
  .net-weight {
    position: absolute;
    left: 0; top: 864px;
    width: 100%;
    text-align: center;
    font-family: "Oswald", sans-serif;
    font-weight: 300;
    font-size: 20px;
    color: var(--weight-grey);
  }
</style>
</head>
<body>
  <main class="bag-front">
    <div class="leaf-pattern-area" role="img" aria-label="Light grey repeating leaf outline pattern"></div>
    <div class="fruit-illustration-area" role="img" aria-label="Black background with faint line drawings of fruits: cherries, strawberries, raspberries, banana, pomegranate, grapes, citrus"></div>
    <div class="gold-divider"></div>

    <svg class="brand-ribbon" viewBox="0 0 92 192" aria-hidden="true">
      <polygon points="0,0 92,0 92,192 46,178 0,192" fill="var(--ribbon-gold)"/>
    </svg>
    <p class="brand-name">AUREL PANTRY</p>

    <h1 class="product-title">POMELO AND<br>COCONUT<br>MEET<br>ALMONDS</h1>

    <div class="product-window" role="img" aria-label="Transparent window showing almonds, coconut cubes and candied pomelo pieces"></div>

    <p class="quality-claim">CERTIFIED QUALITY</p>
    <p class="net-weight">300 G</p>
  </main>
</body>
</html>
```